WERBE-FLYER
Zielgruppe
Immobilien Makler
Aufgabenstellung
Überarbeitung des bestehenden Entwurfs.
Der Flyer wird an Hauseigentümer mit der Post verteilt (nicht adressierte Werbung).
Format:
offen A4 Querformat
geschlossen (1x gefaltet) A5 (4 Seiten)
In der Mitte eine Perforationslinie zum Abtrennen. Danach kann die Seite 3 & 4 zusammengefaltet (geklebt) werden und an uns zurückgeschickt werden.
Rücksendung erfolgt via Geschäftsantwortsendung - ohne Strichcode (siehe Vorlage Alpin. Kurier).

```html
<!DOCTYPE html>
<html lang="de">
<head>
<meta charset="utf-8">
<title>Varona Immobilien AG – Flyer</title>
<link href="https://fonts.googleapis.com/css2?family=Bebas+Neue&family=Oswald:wght@400;500;600&family=Open+Sans:wght@400;600;700&display=swap" rel="stylesheet">
<style>
:root{
  --navy:#0b3357;
  --cyan:#1fb3d1;
  --ink:#333;
  --grey-bg:#efefef;
  --band:#a5a9bc;
  --page:#fff;
  --stage:#e6e6e6;
}
*{box-sizing:border-box;margin:0;padding:0}
html,body{width:1190px;height:1200px;overflow:hidden;background:var(--stage)}
body{position:relative;font-family:"Open Sans",Arial,sans-serif;color:var(--ink)}
.spread{position:absolute;left:195px;width:800px;height:566px;background:var(--page);box-shadow:0 2px 10px rgba(0,0,0,.15);overflow:hidden}
.spread--outside{top:24px}
.spread--inside{top:610px}
.abs{position:absolute}
.head{font-family:"Oswald",Arial,sans-serif;font-weight:500;color:#2f2f2f;text-transform:uppercase;letter-spacing:-.2px;line-height:1.1}
.slash{color:var(--cyan)}

/* reply mark */
.reply-mark{left:200px;top:6px;width:200px;height:92px}
.reply-mark .letter{position:absolute;left:30px;top:6px;font:700 36px "Open Sans",Arial,sans-serif;color:#333}
.reply-mark .note{position:absolute;left:102px;top:18px;font-size:6px;line-height:9px;color:#444}
.reply-mark .caption{position:absolute;left:20px;top:60px;width:180px;font-size:6px;font-weight:700;line-height:9px;text-align:center;color:#333}
.recipient{left:200px;top:160px;font-size:9.5px;font-weight:700;line-height:15px;color:#333}

/* cover */
.cover-photo{left:400px;top:100px;width:365px;height:434px;background:linear-gradient(180deg,#9aa6b3 0%,#c9d0d8 35%,#e8eaec 55%,#b0a89c 78%,#d8d8d6 100%)}
.cover-band{left:400px;top:534px;width:365px;height:32px;background:var(--navy);color:#fff;font:500 13px "Oswald",Arial,sans-serif;display:flex;align-items:center;justify-content:center;letter-spacing:.3px}
.cover-frame{left:402px;top:92px;width:277px;height:338px;border:8px solid var(--navy);border-top-width:9px}
.cover-title{left:428px;top:280px;font:400 54px/48px "Bebas Neue","Oswald",Arial,sans-serif;color:var(--navy);text-transform:uppercase;letter-spacing:0}
.brand{display:flex;align-items:center;gap:6px;font-family:"Oswald",Arial,sans-serif;font-weight:500;color:var(--navy);text-transform:uppercase}
.brand .dot{width:12px;height:12px;background:var(--navy)}
.cover-brand{left:620px;top:40px;font-size:22px}

/* inside left */
.side-label{left:24px;font:600 8px/11px "Oswald",Arial,sans-serif;color:var(--navy);text-transform:uppercase}
.body{font-size:6.6px;line-height:10px;color:#444}
.body p{margin-bottom:9px}
.body ul{list-style:none;margin-bottom:9px}
.body li{position:relative;padding-left:16px}
.body li::before{content:"•";position:absolute;left:2px}
.services{left:112px;top:45px;width:255px}
.services h2{font-size:22px;margin-bottom:10px}
.footer-light{left:0;top:440px;width:388px;height:126px;background:var(--grey-bg)}
.footer-navy{left:100px;top:440px;width:270px;height:126px;background:var(--navy);color:#fff;padding:14px 12px}
.footer-navy h3{font:500 13px "Oswald",Arial,sans-serif;color:var(--cyan);margin-bottom:10px}
.footer-navy .info{font-size:6.6px;line-height:10px}
.footer-brand{left:24px;top:463px;font-size:11px}
.footer-brand .dot{width:7px;height:7px}

/* inside right */
.reply-bg{left:400px;top:0;width:400px;height:566px;background:var(--grey-bg)}
.glue{left:400px;width:400px;height:20px;background:var(--band);color:#eef;font-size:5px;display:flex;align-items:center;justify-content:center;letter-spacing:.3px;text-transform:uppercase}
.perforation{left:399px;top:0;height:566px;border-left:1.5px dashed var(--navy)}
.frame-bar{position:absolute;background:var(--navy)}
.values{left:436px;top:62px;width:330px;padding:0 20px 0 12px}
.values h2{font-size:26px;margin:0 0 14px 0}
.quote-text{left:475px;top:194px;font:400 14px/18px "Oswald",Arial,sans-serif;color:#7b7f90;text-transform:uppercase}
.quote-mark{left:455px;top:190px;font:700 40px/40px "Oswald",Arial,sans-serif;color:var(--cyan)}
.fold-note{left:420px;top:277px;width:360px;border-top:1px solid #bbb;font-size:4.8px;color:#999;text-align:center}
.fold-note span{position:relative;top:-7px;background:var(--grey-bg);padding:0 4px}
.reply{left:436px;top:294px;width:340px}
.reply h2{font-size:22px;margin-bottom:10px}
.checks{list-style:none;margin-top:12px}
.checks li{display:flex;align-items:center;gap:5px;font-size:6.6px;margin-bottom:10px;color:#444}
.checks li::before{content:"";width:9px;height:9px;border:1px solid #888;background:#fff}
.field{position:absolute;width:135px;border-top:1px solid #999;font-size:6.6px;color:var(--navy);padding-top:3px}
</style>
</head>
<body>

<section class="spread spread--outside" aria-label="Aussenseite">
  <div class="abs reply-mark">
    <svg class="abs" width="200" height="92" viewBox="0 0 200 92" aria-hidden="true">
      <g fill="#333">
        <rect x="0" y="2" width="10" height="3"/><rect x="0" y="10" width="10" height="3"/><rect x="0" y="18" width="10" height="3"/>
        <rect x="0" y="26" width="10" height="3"/><rect x="0" y="34" width="10" height="3"/><rect x="0" y="42" width="10" height="3"/>
        <rect x="0" y="50" width="10" height="3"/><rect x="0" y="58" width="10" height="3"/><rect x="0" y="66" width="10" height="3"/>
        <rect x="0" y="74" width="3" height="16"/>
      </g>
      <line x1="0" y1="85" x2="200" y2="85" stroke="#333" stroke-width="10" stroke-dasharray="3 3"/>
    </svg>
    <div class="letter">A</div>
    <div class="note">Nicht frankieren<br>Ne pas affranchir<br>Non affrancare</div>
    <div class="caption">Geschäftsantwortsendung Invio commerciale risposta<br>Envoi commercial-réponse</div>
  </div>
  <div class="abs recipient">VARONA IMMOBILIEN AG<br>Seefeldgasse 17<br>8032 Zürich</div>

  <div class="abs cover-photo" role="img" aria-label="Foto: modernes weisses Einfamilienhaus mit Holzsteg und Kiesgarten unter grauem Himmel"></div>
  <div class="abs cover-frame"></div>
  <h1 class="abs cover-title">Immobilien<br>sind unsere<br>Passion</h1>
  <div class="abs cover-band">VARONA-IMMO.CH</div>
  <div class="abs brand cover-brand"><span class="dot"></span>Varona</div>
</section>

<section class="spread spread--inside" aria-label="Innenseite">
  <div class="abs side-label" style="top:86px">Verkauf mit<br>Passion &amp;<br>Sachverstand</div>
  <div class="abs side-label" style="top:286px">Schätzung des<br>Immobilienwerts</div>

  <div class="abs services body">
    <h2 class="head">Unsere Dienstleistungen <span class="slash">/</span></h2>
    <p>Der Verkauf einer Immobilie ist ein vielschichtiger Prozess.<br>Lieb gewonnene Liegenschaften, die über viele Jahre ein Zuhause waren, haben für die Verkäufer nicht nur einen Geldwert, sondern auch einen emotionalen Wert.</p>
    <p>Wir begleiten unsere Kunden mit Passion und Sachverstand durch jede Phase des Verkaufsprozesses.</p>
    <ul>
      <li>Erstes Gespräch und Besichtigung der Immobilie</li>
      <li>Ermitteln des bestmöglichen Verkaufspreises</li>
      <li>Erstellen von Verkaufsunterlagen und Vermarktung des Objekts</li>
      <li>Qualifizieren der Kaufinteressenten</li>
      <li>Finanzierungsberatung für Kaufinteressenten</li>
      <li>Preisverhandlung und Ausarbeiten des Kaufvertrags</li>
      <li>Begleitung bei der Beurkundung und Eigentumsübertragung</li>
    </ul>
    <p style="margin-top:22px">Damit unsere Kunden den bestmöglichen Preis für ihr Haus, ihre Eigentumswohnung oder ihr Grundstück erzielen, ermitteln wir den genauen Wert. Unsere Schätzung ergibt eine übersichtliche Aufstellung zum Gebäude, der Lage, dem wirtschaftlichen Wert und Angaben zum Verkehrswert der Immobilie.</p>
    <p>Wir wenden je nach Objekt die folgenden Bewertungsmethoden an:</p>
    <ul>
      <li>Sachwert-, Ertragswert- oder Mischwertmethode</li>
      <li>Hedonische Bewertungen, Residualwertverfahren oder DCF (Discounted-Cash-Flow Verfahren)</li>
    </ul>
  </div>

  <div class="abs footer-light"></div>
  <div class="abs brand footer-brand"><span class="dot"></span>Varona</div>
  <div class="abs footer-navy">
    <h3>VARONA IMMOBILIEN AG</h3>
    <div class="info">Seefeldgasse 17<br>8032 Zürich</div>
    <div class="info" style="display:flex;gap:34px;margin-top:12px">
      <div>T: &nbsp;+41 44 555 01 20<br>F: &nbsp;+41 44 555 01 25</div>
      <div>info@varona-immo.ch<br>www.varona-immo.ch</div>
    </div>
  </div>

  <div class="abs reply-bg"></div>
  <div class="abs glue" style="top:0">Klebestreifen</div>
  <div class="abs glue" style="top:546px">Klebestreifen</div>
  <div class="abs perforation"></div>
  <svg class="abs" style="left:392px;top:484px" width="16" height="18" viewBox="0 0 16 18" aria-hidden="true">
    <g fill="none" stroke="var(--cyan)" stroke-width="1.4">
      <circle cx="4" cy="14" r="3"/><circle cx="12" cy="14" r="3"/>
      <line x1="5.5" y1="11.5" x2="12" y2="1"/><line x1="10.5" y1="11.5" x2="4" y2="1"/>
    </g>
  </svg>

  <div class="frame-bar" style="left:436px;top:44px;width:337px;height:7px"></div>
  <div class="frame-bar" style="left:436px;top:44px;width:7px;height:14px"></div>
  <div class="frame-bar" style="left:766px;top:44px;width:7px;height:224px"></div>
  <div class="frame-bar" style="left:436px;top:261px;width:337px;height:7px"></div>
  <div class="frame-bar" style="left:436px;top:188px;width:7px;height:80px"></div>

  <div class="abs values body">
    <h2 class="head">Unsere Werte &amp; Visionen</h2>
    <p>Jede Immobilie ist so einzigartig, wie die Menschen, denen sie gehört. Für uns zählt der Mensch, die Liegenschaft und die gemeinsame Geschichte. In über 20 Jahren haben wir das Immobiliengeschäft und all seine Facetten verinnerlicht. Das macht uns zu einem kompetenten und engagierten Partner für alle Fragen rund um Immobilien.</p>
  </div>
  <div class="abs quote-mark">”</div>
  <div class="abs quote-text">Immobilien sind unsere Passion<br>und die Zufriedenheit der Kunden<br>ist unser Ziel.</div>

  <div class="abs fold-note"><span>Bitte 1x falten und an den Klebestreifen zusammenkleben</span></div>

  <div class="abs reply">
    <h2 class="head">Rückantwort <span class="slash">/</span></h2>
    <div class="body">Bitte kreuzen Sie Ihre Wünsche an:</div>
    <ul class="checks">
      <li>... wir denken über einen Verkauf unserer Immobilie nach</li>
      <li>... wir sind am Kauf einer Wohnung / Haus interessiert</li>
      <li>... wir wünschen ein unverbindliches persönliches Gespräch</li>
    </ul>
  </div>
  <div class="field" style="left:436px;top:444px">Name / Vorname</div>
  <div class="field" style="left:436px;top:478px">Strasse / Nr.</div>
  <div class="field" style="left:600px;top:478px">PLZ / Ort</div>
  <div class="field" style="left:436px;top:512px">Telefon</div>
  <div class="field" style="left:600px;top:512px">E-Mail</div>
</section>

</body>
</html>
```